Top International Talent Management Needs creative business card design

We manage actors careers and book them liaising and promoting their profiles internationally through Casting Directors, Producers, Directors, Publicists etc. We need clearly visable contact details but with a design that reflects our status and creativity of TV, Feature Film industry. Our logo is attached and needs to relate and our website is www.marrowlanepeople.com
No flame designs please but please incorporate logo colours.

Target Market(s)

Clients

Industry/Entity Type

Film Production

Contact Information for Business Card

Director Rosalind Tebbett
Suite F, Building 4, Harrowgate Sound Stages, Tullick Vale, Sydney, NSW 2021

Font styles to use
Sans Serif

Colors
ec1f27

Requirements
Nice to have
• Colours should relate to logo attached and type can relate again to type in the logo design.
Should not have
• No Flames designs and best to be not too obvious with the film designs eiither. Needs to be more creative and modern

```html
<!DOCTYPE html>
<html lang="en">
<head>
<meta charset="utf-8">
<title>Marrow Lane People – Business Card</title>
<link rel="stylesheet" href="https://fonts.googleapis.com/css2?family=Open+Sans:wght@400;600;700&display=swap">
<style>
  :root {
    --backdrop: #ebebeb;
    --card-grey: #d9d9d9;
    --brand-red: #991a1f;
    --logo-red: #d0202a;
    --ink-white: #ffffff;
    --shadow: rgba(0, 0, 0, 0.18);
  }
  * { margin: 0; padding: 0; box-sizing: border-box; }
  html, body {
    width: 1200px;
    height: 900px;
    overflow: hidden;
    background: var(--backdrop);
    font-family: "Open Sans", Arial, sans-serif;
  }
  .canvas {
    position: relative;
    width: 1200px;
    height: 900px;
  }
  .card {
    position: absolute;
    left: 300px;
    width: 600px;
    height: 343px;
    background: var(--card-grey);
    box-shadow: 0 6px 18px var(--shadow);
    overflow: hidden;
  }
  .card--front { top: 60px; }
  .card--back { top: 497px; }

  /* front face */
  .front__band-top {
    position: absolute; left: 0; top: 0;
    width: 100%; height: 96px;
    background: var(--brand-red);
  }
  .front__band-bottom {
    position: absolute; left: 0; top: 280px;
    width: 100%; height: 20px;
    background: var(--brand-red);
  }
  .brand-name {
    color: var(--logo-red);
    font-weight: 700;
    font-size: 32px;
    line-height: 1;
    letter-spacing: 0.5px;
    white-space: nowrap;
  }
  .front__brand {
    position: absolute;
    left: 0; top: 170px;
    width: 100%;
    text-align: center;
  }

  /* back face */
  .back__brand {
    position: absolute;
    right: 40px; top: 80px;
  }
  .back__panel {
    position: absolute; left: 0; top: 128px;
    width: 100%; height: 196px;
    background: var(--brand-red);
    color: var(--ink-white);
  }
  .person {
    position: absolute; left: 24px; top: 14px;
  }
  .person__name {
    font-size: 21px;
    font-weight: 700;
    line-height: 1.15;
  }
  .person__role {
    font-size: 13px;
    font-weight: 400;
  }
  .contact-list {
    position: absolute;
    right: 22px; bottom: 12px;
    list-style: none;
    text-align: right;
  }
  .contact-list__item {
    display: flex;
    justify-content: flex-end;
    align-items: center;
    gap: 8px;
    font-size: 14px;
    line-height: 21px;
    white-space: nowrap;
  }
  .contact-list__icon {
    width: 12px; height: 12px;
    flex: none;
  }
</style>
</head>
<body>
<main class="canvas">

  <section class="card card--front" aria-label="Card front">
    <div class="front__band-top"></div>
    <p class="front__brand brand-name">Marrow Lane People</p>
    <div class="front__band-bottom"></div>
  </section>

  <section class="card card--back" aria-label="Card back">
    <p class="back__brand brand-name">Marrow Lane People</p>
    <div class="back__panel">
      <div class="person">
        <h1 class="person__name">Rosalind Tebbett</h1>
        <p class="person__role">Managing Director</p>
      </div>
      <ul class="contact-list">
        <li class="contact-list__item">02 5550 1847
          <svg class="contact-list__icon" viewBox="0 0 12 12" aria-hidden="true"><path fill="#fff" d="M1 4c0-2 2-3 5-3s5 1 5 3l-2 1-1-1.5H4L3 5zM3 6h6l1 5H2z"/></svg>
        </li>
        <li class="contact-list__item">0400 555 392
          <svg class="contact-list__icon" viewBox="0 0 12 12" aria-hidden="true"><rect x="3" y="0.5" width="6" height="11" rx="1" fill="#fff"/><rect x="4" y="2" width="4" height="6" fill="#991a1f"/></svg>
        </li>
        <li class="contact-list__item">rosalind@marrowlanepeople.com
          <svg class="contact-list__icon" viewBox="0 0 12 12" aria-hidden="true"><rect x="0.5" y="2.5" width="11" height="7" fill="#fff"/><path d="M0.5 2.5L6 7l5.5-4.5" fill="none" stroke="#991a1f" stroke-width="1"/></svg>
        </li>
        <li class="contact-list__item">www.marrowlanepeople.com
          <svg class="contact-list__icon" viewBox="0 0 12 12" aria-hidden="true"><g fill="none" stroke="#fff" stroke-width="1.5"><rect x="0.8" y="5.5" width="6" height="3.5" rx="1.7" transform="rotate(-45 3.8 7.2)"/><rect x="5.2" y="3" width="6" height="3.5" rx="1.7" transform="rotate(-45 8.2 4.7)"/></g></svg>
        </li>
        <li class="contact-list__item">Suite F, Building 4, Harrowgate Sound Stages, Tullick Vale, Sydney, NSW 2021
          <svg class="contact-list__icon" viewBox="0 0 12 12" aria-hidden="true"><path fill="#fff" d="M6 0.5a4 4 0 0 1 4 4c0 3-4 7-4 7s-4-4-4-7a4 4 0 0 1 4-4z"/><circle cx="6" cy="4.5" r="1.5" fill="#991a1f"/></svg>
        </li>
      </ul>
    </div>
  </section>

</main>
</body>
</html>
```